Pinecrest Haulers ~ A+ Division of Vantor

Energetic ,different ,exotic ,modern,
never before done, next level buisness card for a trash dumpster company
is for a trash removal construction company ...please have your wildest ideas i dont want a boring basic buisness card i want people to say wow !! And be able to mention you and who designed my card ...i know you take pride in your work i do to ....3 years ago quillwork from brief hive made a logo for me and i still love it .....use his colors and the word vantor DO NOT USE ROOFING AND REMODELING use Pinecrest Haulers ....look at his Logo i Like the [S] LOGO and word Vantor ....you surprise me and we will do alot more projects with you and or brief hive ....thank you for your hard work and your time i do appreciate all of you and admire your skills designing .....i really do appreciate all of you thank you -todd
Ps Lets make these biz cards special different from many ,unique

Target Market(s)

Construction .....dumpsters trash Trash removal

Industry/Entity Type

Construction

Contact Information for Business Card

Black gold white maybe more colors

Requirements
Must have
• Vantor ~Pinecrest Haulers division Serving Atlanta and surrounding areas'Chief executive Todd Marlow cell 404 555 0147 Office 404 888 8888Follow us on fb ,instagram .. email Pinecresthaulers-demo.com Hablamos espaƱol
Nice to have
• Black gold white colors like my logo i updated and you can add more if you want ....its a construction / trucking company dumpster Trash company we recycle also
Should not have
• When you look at my logo (Must not have roofing and remodeling )

```html
<!DOCTYPE html>
<html lang="en">
<head>
<meta charset="utf-8">
<title>Vantor – Business Card</title>
<link href="https://fonts.googleapis.com/css2?family=Roboto:wght@400;500;900&display=swap" rel="stylesheet">
<style>
  :root {
    --bg: #3a342e;
    --card-black: #1d1b1c;
    --card-black-light: #2c2a2b;
    --gold: #e9b714;
    --gold-light: #f8d82a;
    --gold-deep: #c8960c;
    --gold-text: #d9a21b;
    --white: #ffffff;
    --muted: #cfcac3;
    --ink: #1a1a1a;
  }
  * { margin: 0; padding: 0; box-sizing: border-box; }
  html, body { width: 1200px; height: 930px; overflow: hidden; }
  body {
    background: var(--bg);
    font-family: "Roboto", sans-serif;
    position: relative;
  }
  .card {
    position: absolute;
    width: 620px;
    height: 354px;
    background: linear-gradient(135deg, var(--card-black) 0%, var(--card-black-light) 55%, var(--card-black) 100%);
    box-shadow: 0 10px 28px rgba(0,0,0,0.45);
    overflow: hidden;
  }
  .card--front { left: 120px; top: 70px; }
  .card--back { left: 460px; top: 500px; }

  .brand {
    position: absolute;
    display: flex;
    align-items: center;
    gap: 14px;
  }
  .brand__mark {
    width: 64px; height: 64px;
    background: linear-gradient(135deg, var(--gold-deep), var(--gold-light) 50%, var(--gold-deep));
  }
  .brand__name {
    font-weight: 900;
    font-size: 58px;
    letter-spacing: 1px;
    color: var(--white);
    line-height: 1;
    text-transform: uppercase;
  }
  .card--front .brand { left: 150px; top: 145px; }
  .card--back .brand { left: 48px; top: 62px; }
  .card--back .brand__mark { width: 54px; height: 54px; }
  .card--back .brand__name { font-size: 48px; }

  .division {
    position: absolute;
    left: 48px;
    top: 130px;
    font-size: 13px;
    color: var(--muted);
    letter-spacing: 0.3px;
  }
  .division strong { color: var(--gold-text); font-weight: 500; }

  .card__shapes { position: absolute; inset: 0; }

  .holder {
    position: absolute;
    right: 26px;
    top: 200px;
    text-align: right;
  }
  .holder__name {
    font-weight: 500;
    font-size: 27px;
    color: var(--gold-text);
    text-transform: uppercase;
    letter-spacing: 0.5px;
  }
  .holder__title {
    font-size: 17px;
    color: var(--ink);
    margin-top: 2px;
  }

  .contact {
    position: absolute;
    left: 48px;
    top: 238px;
    list-style: none;
    font-size: 13.5px;
    color: var(--ink);
  }
  .contact li { display: flex; align-items: center; gap: 8px; line-height: 19px; }
  .contact svg { width: 11px; height: 11px; flex: none; }
  .contact__label { font-weight: 500; }
</style>
</head>
<body>

  <section class="card card--front" aria-label="Card front">
    <div class="brand">
      <span class="brand__mark"></span>
      <span class="brand__name">Vantor</span>
    </div>
  </section>

  <section class="card card--back" aria-label="Card back">
    <svg class="card__shapes" viewBox="0 0 620 354" preserveAspectRatio="none" aria-hidden="true">
      <defs>
        <linearGradient id="goldFill" x1="0" y1="1" x2="1" y2="0">
          <stop offset="0" stop-color="#d9a50d"/>
          <stop offset="0.45" stop-color="#f6d51f"/>
          <stop offset="1" stop-color="#e2b315"/>
        </linearGradient>
      </defs>
      <polygon points="330,190 620,190 620,280 470,280" fill="#ffffff"/>
      <polygon points="0,225 290,190 540,354 0,354" fill="url(#goldFill)"/>
    </svg>

    <div class="brand">
      <span class="brand__mark"></span>
      <span class="brand__name">Vantor</span>
    </div>

    <p class="division"><strong>Pinecrest Haulers</strong> division · Serving Atlanta and surrounding areas</p>

    <div class="holder">
      <div class="holder__name">Todd Marlow</div>
      <div class="holder__title">Chief executive</div>
    </div>

    <ul class="contact">
      <li>
        <svg viewBox="0 0 10 14"><rect x="1.5" y="0.8" width="7" height="12.4" rx="1.2" fill="none" stroke="#1a1a1a" stroke-width="1.4"/><circle cx="5" cy="11" r="0.8" fill="#1a1a1a"/></svg>
        <span><span class="contact__label">Cell</span> 404 555 0147</span>
      </li>
      <li>
        <svg viewBox="0 0 12 12"><path d="M2.4 0.8 L4.4 3.3 L3.3 4.6 C4 6 5.8 7.9 7.4 8.7 L8.7 7.6 L11.2 9.6 L9.9 11.2 C5.6 11 1 6.4 0.8 2.1 Z" fill="#1a1a1a"/></svg>
        <span><span class="contact__label">Office</span> 404 555 0162</span>
      </li>
      <li>
        <svg viewBox="0 0 12 12"><circle cx="6" cy="6" r="5" fill="none" stroke="#1a1a1a" stroke-width="1.2"/><ellipse cx="6" cy="6" rx="2.2" ry="5" fill="none" stroke="#1a1a1a" stroke-width="1"/><line x1="1" y1="6" x2="11" y2="6" stroke="#1a1a1a" stroke-width="1"/></svg>
        www.Pinecresthaulers-demo.com
      </li>
      <li>
        <svg viewBox="0 0 12 12"><circle cx="3" cy="6" r="1.8" fill="#1a1a1a"/><circle cx="9.5" cy="2.5" r="1.8" fill="#1a1a1a"/><circle cx="9.5" cy="9.5" r="1.8" fill="#1a1a1a"/><path d="M3 6 L9.5 2.5 M3 6 L9.5 9.5" stroke="#1a1a1a" stroke-width="1"/></svg>
        Follow us on fb · instagram
      </li>
      <li>
        <svg viewBox="0 0 12 12"><path d="M1 1.5 H11 V8 H5 L2.5 10.5 V8 H1 Z" fill="none" stroke="#1a1a1a" stroke-width="1.2" stroke-linejoin="round"/></svg>
        Hablamos español
      </li>
    </ul>
  </section>

</body>
</html>
```